Short-Term Rental Website - Management Services for Property Owner

We are looking for a website to advertise our short-term rental business, Bright Door Rental Management, currently www.brightdoorstays.ca. Hosted on WordPress.

We have the website main page language but we are looking for someone who is creative and can present the information in a trendy, cool and professional way. I like the closed design crowd job "Plumwick Media - SEM, Influencer website. FUN RETRO VIBES" (see attached pictures) in terms of how the page flows, icons and stock images, other connective imagery and design features

Our main competitor website is www.hostvela.com and we like how that website feels but we like the elegance of www.Torvane-Alsky.com (desktop) and main page of www.quorrin.ca (desktop version). We like the slow type video on quorrin.com.

MUST LOOK GOOD ON MOBILE. The mobile experience has to be good.

The content in terms of the language is in one of the attached files.

Our landing page requires the following sections;
- Revenue Maximization
- Services (I have included the content that we want highlighted but we are looking for someone to be creative with how these are displayed
- Pricing
- Featured Properties (display on a carousel) *must design a carousel that can be easily populated.
- Reviews (display on a carousel) *must design a carousel that can be easily populated.
- Contact Us (first name, last name, email, phone (required), description of property)

The header will have;
- Logo (link to main page)
- Pricing (link to pricing section found on the main page)
- Services (link to services section found on the main page)
- Properties (separate page)
- Contact (link to contact area on main page)

We would also need a coded template page that we could use to add additional pages as needed.

For the properties page, we need a landing page that would allow our guests to see all of our properties and a map view with the properties plotted on the map.

As we would collect personal information we would need a cookies/ privacy policy.

The colour palette should be on the light side. We do not want the website to have a dark feel. Colours should be consistent with that of our logo but we are open to creativity.

Investment property owners

Real Estate

2 page

Sans Serif

• Very strong and well designed landing page

Second page which showcases properttes

Template property page that can be easily reproduced

```html
<!DOCTYPE html>
<html lang="en">
<head>
<meta charset="utf-8">
<title>Bright Door Rental Management – Featured Properties &amp; Reviews</title>
<link rel="stylesheet" href="https://fonts.googleapis.com/css2?family=Montserrat:wght@700;800&family=Figtree:ital,wght@0,400;0,500;0,600;1,400&display=swap">
<style>
  :root{
    --ink:#3f3f3f;
    --text:#333333;
    --muted:#8a8a8a;
    --review-text:#7a7a7a;
    --accent-blue:#1f5bb5;
    --accent-mint:#6fe3a4;
    --teal:#4d7d87;
    --star-teal:#4f7f89;
    --star-gold:#f0b43c;
    --rule:#e6e6e6;
    --white:#ffffff;
    --card-shadow:0 3px 6px rgba(0,0,0,.22);
  }
  *{box-sizing:border-box;margin:0;padding:0}
  html,body{width:1200px;height:1200px;overflow:hidden;background:var(--white)}
  body{position:relative;font-family:"Figtree",Arial,sans-serif;color:var(--text)}

  .top-rule{position:absolute;left:101px;top:101px;width:1005px;height:2px;background:var(--rule)}

  .section-title{position:absolute;left:0;width:1200px;text-align:center;font-family:"Montserrat",Arial,sans-serif;font-weight:800;font-size:36px;letter-spacing:-.5px}
  .section-title::after{content:"";position:absolute;left:580px;width:37px;height:2px}
  .featured .section-title{top:168px;color:var(--ink)}
  .featured .section-title::after{top:45px;background:var(--accent-blue)}

  .carousel-count{position:absolute;left:925px;top:253px;font-size:12px;color:var(--muted)}
  .carousel-btn{position:absolute;top:250px;width:23px;height:23px}
  .carousel-btn.prev{left:962px}
  .carousel-btn.next{left:988px}

  .property-card{position:absolute;top:286px;height:285px;background:var(--white);border-radius:15px;box-shadow:var(--card-shadow);overflow:hidden}
  .property-photo{height:175px}
  .property-body{padding:17px 22px 0}
  .property-name{font-size:12px;font-weight:400;line-height:14.5px;color:var(--text);height:29px}
  .property-price{margin-top:8px;font-size:15px;color:var(--text)}
  .property-price span{font-size:11px;color:var(--muted)}
  .property-rating{margin-top:4px;display:flex;align-items:center;gap:7px;font-size:11.5px;color:var(--muted)}
  .stars-small{display:block}

  .reviews{position:absolute;left:101px;top:652px;width:1005px;height:454px;background:var(--teal)}
  .reviews .section-title{left:-101px;top:47px;color:var(--white)}
  .reviews .section-title::after{top:45px;background:var(--accent-mint)}

  .review-arrow{position:absolute;width:28px;height:22px}
  .review-arrow.prev{left:27px;top:222px}
  .review-arrow.next{left:940px;top:232px}

  .review{position:absolute;top:137px;width:400px}
  .review-card{position:relative;height:162px;background:var(--white);border-radius:3px}
  .review-card::after{content:"";position:absolute;left:188px;bottom:-18px;border-left:8px solid transparent;border-right:8px solid transparent;border-top:18px solid var(--white)}
  .review-stars{position:absolute;left:50%;top:19px;width:90px;height:15px;margin-left:-45px;display:block}
  .quote-mark{position:absolute;left:18px;top:30px;font-family:"Montserrat",Arial,sans-serif;font-weight:800;font-size:44px;line-height:1;color:#c9c9c9}
  .review-text{position:absolute;left:47px;right:40px;top:56px;font-style:italic;font-size:11.5px;line-height:14.4px;color:var(--review-text)}
  .reviewer{position:absolute;top:196px;left:166px;width:60px;text-align:center}
  .reviewer-photo{width:60px;height:60px;border-radius:50%;border:3px solid var(--accent-mint)}
  .reviewer-name{margin-top:9px;font-size:11px;font-weight:500;color:var(--accent-mint);white-space:nowrap;margin-left:-40px;margin-right:-40px}
  .reviewer-date{font-size:8.5px;font-weight:600;color:var(--white);white-space:nowrap;margin-left:-40px;margin-right:-40px}

  .dots{position:absolute;left:483px;top:441px;display:flex;gap:3px}
  .dots span{width:7px;height:7px;border-radius:50%;background:var(--white)}
</style>
</head>
<body>
  <div class="top-rule"></div>

  <section class="featured">
    <h2 class="section-title">FEATURED PROPERTIES</h2>
    <div class="carousel-count">3/18</div>
    <svg class="carousel-btn prev" viewBox="0 0 24 24" aria-label="Previous"><circle cx="12" cy="12" r="11" fill="none" stroke="#555" stroke-width="1.2"/><path d="M14 7l-5 5 5 5" fill="none" stroke="#444" stroke-width="2.2"/></svg>
    <svg class="carousel-btn next" viewBox="0 0 24 24" aria-label="Next"><circle cx="12" cy="12" r="11" fill="none" stroke="#555" stroke-width="1.2"/><path d="M10 7l5 5-5 5" fill="none" stroke="#444" stroke-width="2.2"/></svg>

    <article class="property-card" style="left:186px;width:260px">
      <div class="property-photo" role="img" aria-label="Bright corner living room with floor-to-ceiling windows and city view" style="background:linear-gradient(160deg,#c9d3dc 0%,#9aa6b0 45%,#5b5f63 75%,#c9a94a 100%)"></div>
      <div class="property-body">
        <h3 class="property-name">Parking, A+ AMENITIES &amp; view! Walk to the game!</h3>
        <p class="property-price">$146 <span>/night</span></p>
        <div class="property-rating">
          <svg class="stars-small" width="46" height="9" viewBox="0 0 50 10"><g fill="var(--star-teal)"><path id="s" d="M5 0l1.3 3.3 3.6.2-2.8 2.3.9 3.5L5 7.4 2 9.3l.9-3.5L.1 3.5l3.6-.2z"/><use href="#s" x="10"/><use href="#s" x="20"/><use href="#s" x="30"/><use href="#s" x="40"/></g></svg>
          36 reviews
        </div>
      </div>
    </article>

    <article class="property-card" style="left:468px;width:263px">
      <div class="property-photo" role="img" aria-label="Suite living area with hardwood floor, fireplace and bedroom beyond" style="background:linear-gradient(150deg,#7a5a3a 0%,#b88a4e 40%,#d9a868 60%,#3d4550 85%,#7fa4b8 100%)"></div>
      <div class="property-body">
        <h3 class="property-name">Snazzy Suite on Trendy West-End by Prince’s Island.</h3>
        <p class="property-price">$146 <span>/night</span></p>
        <div class="property-rating">
          <svg class="stars-small" width="46" height="9" viewBox="0 0 50 10"><g fill="var(--star-teal)"><use href="#s"/><use href="#s" x="10"/><use href="#s" x="20"/><use href="#s" x="30"/><use href="#s" x="40"/></g></svg>
          9 reviews
        </div>
      </div>
    </article>

    <article class="property-card" style="left:750px;width:263px">
      <div class="property-photo" role="img" aria-label="Rooftop patio lounge with green wall and city towers" style="background:linear-gradient(175deg,#9aa0ab 0%,#b4b7bf 35%,#5e7f52 55%,#6d6a66 78%,#9fa6ad 100%)"></div>
      <div class="property-body">
        <h3 class="property-name">Private Rooftop in Beautiful Eau Claire + Parking</h3>
        <p class="property-price">$224 <span>/night</span></p>
        <div class="property-rating">
          <svg class="stars-small" width="46" height="9" viewBox="0 0 50 10"><g fill="var(--star-teal)"><use href="#s"/><use href="#s" x="10"/><use href="#s" x="20"/><use href="#s" x="30"/><use href="#s" x="40"/></g></svg>
          356 reviews
        </div>
      </div>
    </article>
  </section>

  <section class="reviews">
    <h2 class="section-title">REVIEWS</h2>

    <svg class="review-arrow prev" viewBox="0 0 28 22" aria-label="Previous review"><path d="M26 11H4M12 2L3 11l9 9" fill="none" stroke="var(--accent-mint)" stroke-width="3.5"/></svg>
    <svg class="review-arrow next" viewBox="0 0 28 22" aria-label="Next review"><path d="M2 11h22M16 2l9 9-9 9" fill="none" stroke="var(--accent-mint)" stroke-width="3.5"/></svg>

    <article class="review" style="left:85px">
      <div class="review-card">
        <svg class="review-stars" viewBox="0 0 94 15"><g fill="var(--star-gold)"><path id="g" d="M7.5 0l2 5 5.3.3-4.1 3.4 1.4 5.2-4.6-2.9-4.6 2.9 1.4-5.2L.2 5.3 5.5 5z"/><use href="#g" x="19"/><use href="#g" x="38"/><use href="#g" x="57"/><use href="#g" x="76"/></g></svg>
        <div class="quote-mark">“</div>
        <p class="review-text">This place has lot's of amenities and a great, responsive host. It was a good size for two couples to share. I enjoyed having the big patio to relax in the mornings and the deep soak tub to sit in at the end of the day! This is a high-end place to spend your vacation.</p>
      </div>
      <div class="reviewer">
        <div class="reviewer-photo" role="img" aria-label="Reviewer portrait" style="background:linear-gradient(180deg,#e8e8e8,#c9b79a)"></div>
        <p class="reviewer-name">Dana R.</p>
        <p class="reviewer-date">May 2020</p>
      </div>
    </article>

    <article class="review" style="left:510px">
      <div class="review-card">
        <svg class="review-stars" viewBox="0 0 94 15"><g fill="var(--star-gold)"><use href="#g"/><use href="#g" x="19"/><use href="#g" x="38"/><use href="#g" x="57"/><use href="#g" x="76"/></g></svg>
        <div class="quote-mark">“</div>
        <p class="review-text">Such an epic apartment. Amazing view of stampede grounds and downtown (especially from the master bedroom) Really stylish place. Super prompt replies. Will 100% stay here again!</p>
      </div>
      <div class="reviewer">
        <div class="reviewer-photo" role="img" aria-label="Reviewer portrait" style="background:linear-gradient(180deg,#a39a86,#6f6650)"></div>
        <p class="reviewer-name">Owen K.</p>
        <p class="reviewer-date">February 2020</p>
      </div>
    </article>

    <div class="dots"><span></span><span></span><span></span></div>
  </section>
</body>
</html>
```